Hey,
My name is Tomas Vellanegra and I'm starting a PhD in Physics next year. I want to a bit more than just research on my own. I want to bring some public involvement to it.
"Zeta Quarks" is website/wordpress/blog. It is a way to bring physics to the general public without losing the math or the physics essence - This is a place to share fun and interesting findings that PhD students, Professors, High school students and basically everyone else that loves and wants to know a bit more about nature. The idea is to put real science to debate in a open non-judgmental way in prol of knowledge and discovery. "Everybody" is welcome to post relevant things such as experiments made at home as well as their latest discovery in their super high tech £100M lab.
The first step of the project is to develop a BLOG (Wordpress) - the domain is already register "zetaquarks.org and zetaquarks.com" that could host that initial debate and posts.
Think http://lensmoravia.org/ ; http://www.wavecellar.org/; https://www.youtube.com/user/ninetyglyphs; https://www.youtube.com/user/secondquanta as a guidelines...
http://trevilo.bvx.com.br/
I would enjoy touches of watercolour design here and there.
I also like pastel colours. But remember, I am a scientist and not at all designer. I'll trust the artists to create and show me what they are up to.
UPDATE: Just so you guys know. I want to do a Website in form of a Blog. I want to easily post and upload videos and articles related to Physics.
I'm more familiar with Wordpress but if you say that any other platform does the job better and I can still maintain the domain zetaquarks.org lets do it!
Update number 2: I will respond every designer asap. I will however do that between 9:00am and 14:00 pm Brasilia/Brazil Time.
So please don't get upset or take it personal if you don't get a feedback right away, specially if it is 02:00 a.m my time, ok ?! : - )
Thanks Guys and good work!
For all designers that just want to do logos please post them in: Manage Project | Zeta Quarks - Logo Design Project
We will continue from there!
Target Market(s)
Everyone that likes physics, no matter if you are a Nobel Laureate or a single mother that likes physics.
Industry/Entity Type
Artists
Font styles to use
Other font styles liked:
- I like Calibri, Helvetica, Verdana, Univers and Tahoma for body text, Sometimes I use Arial. Cambria and Georgia for headings
Requirements
Must have
- I'm open minded! But I like thinks to be simple!
Nice to have
- The way you going to put "Zeta Quarks" is completely up to you. I usually like it simple but. Show me what you got and I'll give you feedback if I like it or not! Just remember to keep it clean and user friendly.
Should not have
- Just try beautiful and functional designs. I usually don't like super old style fonts like Times New Roman and very elaborate things that are hard to read.

```html
<!DOCTYPE html>
<html lang="en">
<head>
<meta charset="utf-8">
<title>Zeta Quarks — Physics Blog</title>
<link href="https://fonts.googleapis.com/css2?family=Carlito:wght@400;700&display=swap" rel="stylesheet">
<style>
:root{
  --red:#e8463c;
  --teal:#2b9c8e;
  --teal-light:#7cc6b3;
  --blue:#2f7fb0;
  --text:#555;
  --muted:#888;
  --line:#e2e2e2;
  --nav-bg:#f4f4f4;
  --author-bg:#d9e7f3;
  --footer-bg:#2a2a2a;
  --footer-text:#bdbdbd;
}
*{box-sizing:border-box;margin:0;padding:0}
html,body{width:1200px;height:2344px;overflow:hidden}
body{position:relative;background:#fff;font-family:"Carlito",Calibri,Arial,sans-serif;color:var(--text)}
.abs{position:absolute}

/* header */
.logo{left:100px;top:30px;display:flex;align-items:center;gap:12px;font-size:46px;font-weight:700;color:var(--red);letter-spacing:-.5px}
.logo-mark{width:26px;height:26px;border-radius:50%;background:var(--red)}
.social{left:780px;top:42px;display:flex;gap:10px}
.social span{width:32px;height:32px;border-radius:50%;background:#3a3a3a;display:block}
.social span:nth-child(2){background:#3b8fd0}
.social span:nth-child(3){background:#d9473b}
.social span:nth-child(5){background:#c33}
.login{left:1020px;top:32px;width:92px;height:54px;background:var(--teal-light);color:#fff;font-size:18px;display:flex;align-items:center;justify-content:center;gap:8px}
.nav{left:100px;top:118px;width:1012px;height:36px;background:var(--nav-bg);border-top:2px solid var(--line);border-bottom:1px solid var(--line);display:flex;align-items:center;font-size:15px}
.nav a{color:#555;text-decoration:none;padding:0 30px;line-height:34px;border-right:1px solid var(--line)}
.nav a.active{color:var(--teal);border-top:3px solid var(--teal);margin-top:-3px;background:#fff}
.nav .search{margin-left:auto;margin-right:26px}

/* hero */
.hero{left:100px;top:192px;width:1012px;height:328px;background:linear-gradient(100deg,#0d2a1c 0%,#2c6a3c 30%,#1a1a1a 60%,#050505 100%)}
.hero-caption{left:780px;top:292px;width:300px;font-size:30px;line-height:34px;color:#f2a23a}
.hero-dots{left:1040px;top:490px;display:flex;gap:8px}
.hero-dots i{width:9px;height:9px;border-radius:50%;background:#fff;opacity:.6;display:block}
.hero-dots i:first-child{opacity:1}

/* posts */
.post{left:100px;width:700px;height:200px;display:flex;gap:24px}
.post + .sep{}
.thumb{width:220px;height:160px;flex:none;position:relative}
.play{position:absolute;left:86px;top:56px;width:48px;height:48px;border-radius:8px;background:rgba(0,0,0,.7);display:flex;align-items:center;justify-content:center}
.post-body{flex:1}
.post-title{font-size:24px;line-height:26px;color:var(--blue);font-weight:400}
.post-date{font-size:12px;color:var(--red);margin:6px 0 8px}
.post-date b{color:var(--blue);font-weight:400}
.post-excerpt{font-size:12px;line-height:16px;color:var(--muted)}
.share{display:flex;gap:8px;margin-top:10px}
.share span{width:28px;height:28px;border-radius:50%;background:#a9a9a9;display:block}
.rule{left:100px;width:700px;height:1px;background:var(--line)}

.author{background:var(--author-bg);padding:18px 16px;font-size:13px;color:#4a6a86}
.author-head{display:flex;align-items:center;gap:12px;margin-bottom:18px}
.avatar{width:50px;height:50px;border-radius:50%;background:#c98d6a;border:3px solid #fff}
.author-name{font-size:17px;color:var(--blue)}
.author-meta{display:flex;align-items:center;gap:8px;margin-top:8px}
.author-meta i{width:12px;height:10px;background:#7b9bb8;display:block}

.pager{left:330px;top:2018px;display:flex;gap:4px}
.pager span{width:22px;height:20px;border:1px solid #bbb;font-size:11px;display:flex;align-items:center;justify-content:center;color:#777}
.pager span.on{background:#666;color:#fff;border-color:#666}

/* sidebar */
.side-title{left:832px;font-size:24px;color:var(--teal);width:280px}
.side-title.red{color:var(--red);display:flex;align-items:center;gap:8px}
.side-item{left:832px;width:280px;display:flex;gap:12px}
.side-img{width:80px;height:80px;flex:none}
.side-text{font-size:12px;line-height:15px;color:var(--muted);padding-top:6px}
.news-input{left:832px;top:1092px;width:220px;height:32px;border:1px solid #ccc;font-size:12px;color:#aaa;padding:8px}
.news-btn{left:1052px;top:1092px;width:60px;height:32px;background:var(--red)}
.feed{left:832px;top:1680px;width:280px;height:330px;border:1px solid var(--line);padding:14px 14px}
.tweet{background:#f7f9fa;border:1px solid #e6e6e6;padding:10px;font-size:12px;line-height:15px;color:#777;margin-bottom:14px}
.tweet b{color:var(--blue);font-weight:400}
.tweet a{color:var(--blue);text-decoration:none}

/* footer */
.footer{left:0;top:2080px;width:1200px;height:264px;background:var(--footer-bg)}
.foot-nav{left:0;top:2112px;width:1200px;display:flex;justify-content:center;gap:30px;font-size:13px;color:var(--footer-text)}
.foot-nav span::before{content:"•";margin-right:6px;color:#777}
.copyright{left:100px;top:2186px;font-size:13px;color:#8a8a8a}
.foot-icons{left:1040px;top:2176px;display:flex;gap:10px}
.foot-icons span{width:34px;height:34px;border-radius:50%;background:#555;display:flex;align-items:center;justify-content:center}
</style>
</head>
<body>

<header>
  <div class="abs logo"><span class="logo-mark"></span>Zeta Quarks</div>
  <div class="abs social"><span></span><span></span><span></span><span></span><span></span></div>
  <div class="abs login">
    <svg width="14" height="16" viewBox="0 0 14 16"><rect x="1" y="7" width="12" height="8" rx="1" fill="#fff"/><path d="M3.5 7V4.5a3.5 3.5 0 0 1 7 0V7" stroke="#fff" stroke-width="2" fill="none"/></svg>Login
  </div>
  <nav class="abs nav">
    <a class="active">Home</a><a>About us</a><a>The Nature</a><a>Categories</a><a>Upload Article</a><a>FAQ</a>
    <svg class="search" width="16" height="16" viewBox="0 0 16 16"><circle cx="6.5" cy="6.5" r="5" stroke="#444" stroke-width="2" fill="none"/><line x1="10" y1="10" x2="15" y2="15" stroke="#444" stroke-width="2.4"/></svg>
  </nav>
</header>

<section>
  <div class="abs hero" role="img" aria-label="Researcher in safety goggles working at a green laser optics bench"></div>
  <p class="abs hero-caption">Etiam varius leo vitae mauri pretium eleifend.</p>
  <div class="abs hero-dots"><i></i><i></i><i></i><i></i></div>
</section>

<main>
  <article class="abs post" style="top:548px">
    <div class="thumb author">
      <div class="author-head"><div class="avatar" role="img" aria-label="Author portrait"></div><span class="author-name">Ravi Dunmore</span></div>
      <div class="author-meta"><i></i>Tag name</div>
      <div class="author-meta"><i></i>Category name</div>
    </div>
    <div class="post-body">
      <h2 class="post-title">Aenean fringilla neque tristique elit ultricies commodo facilisis</h2>
      <p class="post-date">Sep 1, 2014 · <b>10 Comments</b></p>
      <p class="post-excerpt">Morbi in mauris nisi. Praesent ut congue lacus, in sagittis nunc. Duis tempor porta ipsum, sit amet lobortis purus in faucibus. Sed volutpat consequat nibh, quis blandit diam.</p>
      <div class="share"><span></span><span></span><span></span><span></span></div>
    </div>
  </article>
  <div class="abs rule" style="top:764px"></div>

  <article class="abs post" style="top:780px">
    <div class="thumb" role="img" aria-label="Red and grey chequered test pattern with video play button" style="background:linear-gradient(135deg,#8a1d1d,#c7c7c7 60%,#6b6b6b)">
      <div class="play"><svg width="18" height="20" viewBox="0 0 18 20"><path d="M2 1l15 9-15 9z" fill="#fff"/></svg></div>
    </div>
    <div class="post-body">
      <h2 class="post-title">Curabitur sollicitudin odio ligula, ultricies porttitor tellus vestibulum</h2>
      <p class="post-date">Sep 1, 2014 · <b>10 Comments</b></p>
      <p class="post-excerpt">Morbi in mauris nisi. Praesent ut congue lacus, in sagittis nunc. Duis tempor porta ipsum, sit amet lobortis purus in faucibus. Sed volutpat consequat nibh, quis blandit diam.</p>
      <div class="share"><span></span><span></span><span></span><span></span></div>
    </div>
  </article>
  <div class="abs rule" style="top:996px"></div>

  <article class="abs post" style="top:1012px">
    <div class="thumb" role="img" aria-label="Row of steel balls of a swinging pendulum toy" style="background:linear-gradient(120deg,#1d1d1d,#6a5a4a 50%,#2a2a2a)"></div>
    <div class="post-body">
      <h2 class="post-title">Cras iaculis aliquam diam, eu ultrices magna semper etamet</h2>
      <p class="post-date">Sep 1, 2014 · <b>10 Comments</b></p>
      <p class="post-excerpt">Morbi in mauris nisi. Praesent ut congue lacus, in sagittis nunc. Duis tempor porta ipsum, sit amet lobortis purus in faucibus. Sed volutpat consequat nibh, quis blandit diam.</p>
      <div class="share"><span></span><span></span><span></span><span></span></div>
    </div>
  </article>
  <div class="abs rule" style="top:1224px"></div>

  <article class="abs post" style="top:1240px">
    <div class="thumb" role="img" aria-label="Colourful glowing galaxy in deep space" style="background:radial-gradient(circle at 50% 50%,#e8c35a,#b34a2c 30%,#1b2a5a 65%,#05060f)"></div>
    <div class="post-body">
      <h2 class="post-title">Vivamus facilisis erat ac purus sestibulum, quis luctus turpis iaculis</h2>
      <p class="post-date">Sep 1, 2014 · <b>10 Comments</b></p>
      <p class="post-excerpt">Morbi in mauris nisi. Praesent ut congue lacus, in sagittis nunc. Duis tempor porta ipsum, sit amet lobortis purus in faucibus. Sed volutpat consequat nibh, quis blandit diam.</p>
      <div class="share"><span></span><span></span><span></span><span></span></div>
    </div>
  </article>
  <div class="abs rule" style="top:1456px"></div>

  <article class="abs post" style="top:1472px">
    <div class="thumb" role="img" aria-label="Orange sparks of light on dark background with video play button" style="background:radial-gradient(circle at 40% 50%,#f0a030,#8a3a10 40%,#120805)">
      <div class="play"><svg width="18" height="20" viewBox="0 0 18 20"><path d="M2 1l15 9-15 9z" fill="#fff"/></svg></div>
    </div>
    <div class="post-body">
      <h2 class="post-title">Sed sagittis mi sit amet est bibendum, porttitor dictum sapien loborti</h2>
      <p class="post-date">Sep 1, 2014 · <b>10 Comments</b></p>
      <p class="post-excerpt">Morbi in mauris nisi. Praesent ut congue lacus, in sagittis nunc. Duis tempor porta ipsum, sit amet lobortis purus in faucibus. Sed volutpat consequat nibh, quis blandit diam.</p>
      <div class="share"><span></span><span></span><span></span><span></span></div>
    </div>
  </article>
  <div class="abs rule" style="top:1688px"></div>

  <article class="abs post" style="top:1704px">
    <div class="thumb" role="img" aria-label="Passenger jet on runway under blue sky" style="background:linear-gradient(180deg,#6aa8d8,#c8dcec 60%,#8a8f94)"></div>
    <div class="post-body">
      <h2 class="post-title">Phasellus sit amet felis sed libero iaculis egestas habitant.</h2>
      <p class="post-date">Sep 1, 2014 · <b>10 Comments</b></p>
      <p class="post-excerpt">Morbi in mauris nisi. Praesent ut congue lacus, in sagittis nunc. Duis tempor porta ipsum, sit amet lobortis purus in faucibus. Sed volutpat consequat nibh, quis blandit diam.</p>
      <div class="share"><span></span><span></span><span></span><span></span></div>
    </div>
  </article>

  <div class="abs pager"><span class="on">1</span><span>2</span><span>3</span><span>4</span><span>5</span><span>6</span><span>7</span><span>8</span><span>›</span></div>
</main>

<aside>
  <h3 class="abs side-title" style="top:552px">Top Articles</h3>
  <div class="abs side-item" style="top:590px"><div class="side-img" role="img" aria-label="Glowing nebula" style="background:linear-gradient(135deg,#1a2a6a,#8a6ad0)"></div><p class="side-text">Nam libero justo, feugiat nec faugiat in, porta at lorem.</p></div>
  <div class="abs side-item" style="top:680px"><div class="side-img" role="img" aria-label="Colourful sparks" style="background:linear-gradient(135deg,#3a1a4a,#e06a3a)"></div><p class="side-text">Nam libero justo, feugiat nec faugiat in, porta at lorem.</p></div>
  <div class="abs side-item" style="top:770px"><div class="side-img" role="img" aria-label="Rainbow light prism" style="background:linear-gradient(135deg,#2a4ab0,#d04ab0 50%,#e0c040)"></div><p class="side-text">Nam libero justo, feugiat nec faugiat in, porta at lorem.</p></div>
  <div class="abs side-item" style="top:860px"><div class="side-img" role="img" aria-label="Blue glowing particle tracks" style="background:linear-gradient(135deg,#050a2a,#2a5ad0)"></div><p class="side-text">Nam libero justo, feugiat nec faugiat in, porta at lorem.</p></div>

  <h3 class="abs side-title red" style="top:1048px"><svg width="22" height="16" viewBox="0 0 22 16"><rect width="22" height="16" rx="2" fill="#e8463c"/><path d="M1 2l10 7 10-7" stroke="#fff" stroke-width="1.6" fill="none"/></svg>Newsletter Signup</h3>
  <div class="abs news-input">Email address</div>
  <div class="abs news-btn"></div>

  <h3 class="abs side-title" style="top:1160px">Most Viewed</h3>
  <div class="abs side-item" style="top:1200px"><div class="side-img" role="img" aria-label="Hand holding glowing lamp" style="background:linear-gradient(135deg,#2a2a2a,#c89a5a)"></div><p class="side-text">Nam libero justo, feugiat nec faugiat in, porta at lorem.</p></div>
  <div class="abs side-item" style="top:1290px"><div class="side-img" role="img" aria-label="Balls in motion" style="background:linear-gradient(135deg,#4a4a4a,#bababa)"></div><p class="side-text">Nam libero justo, feugiat nec faugiat in, porta at lorem.</p></div>
  <div class="abs side-item" style="top:1380px"><div class="side-img" role="img" aria-label="Bright lightning over landscape" style="background:linear-gradient(135deg,#1a1a3a,#5a7ad0)"></div><p class="side-text">Nam libero justo, feugiat nec faugiat in, porta at lorem.</p></div>
  <div class="abs side-item" style="top:1470px"><div class="side-img" role="img" aria-label="Green landscape with sky" style="background:linear-gradient(180deg,#8ac0e0,#5a9a4a)"></div><p class="side-text">Nam libero justo, feugiat nec faugiat in, porta at lorem.</p></div>

  <h3 class="abs side-title" style="top:1640px">Chirper Feed</h3>
  <div class="abs feed">
    <div class="tweet"><b>Zeta Labs</b> @zetaquarks<br>Nulla tincidunt elit a mauris pulvinar molestie. <a>Nulla euismod risus ac</a> lorem vehicula <a>tristique.</a><br><a>Reply · Retweet · Favorite</a></div>
    <div class="tweet"><b>Zeta Labs</b> @zetaquarks<br>Nulla tincidunt elit a mauris pulvinar molestie. <a>Nulla euismod risus ac</a> lorem vehicula <a>tristique.</a><br><a>Reply · Retweet · Favorite</a></div>
  </div>
</aside>

<footer>
  <div class="abs footer"></div>
  <nav class="abs foot-nav"><span>Home</span><span>About us</span><span>Categories</span><span>FAQ</span><span>Students</span><span>Professors</span><span>Upload Article</span><span>Register</span><span>Login</span></nav>
  <p class="abs copyright">Copyright © 2014 Zeta Quarks . All rights reserved.</p>
  <div class="abs foot-icons">
    <span><svg width="14" height="14" viewBox="0 0 14 14"><rect x="1" y="3" width="12" height="9" fill="none" stroke="#ddd" stroke-width="1.6"/><path d="M1 3l6 5 6-5" stroke="#ddd" stroke-width="1.4" fill="none"/></svg></span>
    <span><svg width="14" height="14" viewBox="0 0 14 14"><path d="M2 10l5-6 5 6" stroke="#ddd" stroke-width="2" fill="none"/></svg></span>
  </div>
</footer>

</body>
</html>
```